Création de Brochure A6
Besoins
Nous avons besoin d'une Brochure A6 de 4 pages pour notre société qui sera destinée à des cours de soutien pour Classe préparatoires et Terminale, La Brochure doit idéalement être en Orange, Gris très foncé et Blanc. La fonction principale de la Brochure sera de faire connaitre notre établissement aux étudiants des classes préparatoires. L'établissement sera basé au Maroc. N'hésitez pas à utiliser des images qui reflètent le monde de l'éducation. vous trouverez ci-joint les document nécessaires. Si vous voulez utiliser des images qui vous appartient n'hésitez pas. si vous avez des remarques liés à la formulation des phrases contenues dans la documentation, n'hésitez pas à les reformuler, soyez libre!
Merci de nous fournir à l'issue du concours des fichiers modifiables.
Bon courage!
Description de l'entreprise
La prestation proposée par notre société consiste à proposer à l’ensemble des étudiants des classes préparatoires et du lycée des cours de soutien scolaire. Les matières concernées ce sont notamment des matières scientifiques. Moyennant des outils technologique et pédagogiques de pointe, notre société propose aux élèves et aux étudiants des cours de soutien scolaire à travers des professeurs compétents et pédagogues à la fois, notre société aura recours à des étudiants des grandes écoles d’ingénieurs françaises pour effectuer des stages intensifs pour les étudiants des classes préparatoires. La prestation offerte par notre société intègre également des support de cours en format électronique disponible sur l’intranet de notre site internet, des Forums de discussions et des Tutoriels Vidéo.
L’objectif de la prestation est d’offrir aux élèves et aux étudiants un environnement de préparation optimale aux différents concours et examens.
Couleurs, favoris et autres exigences:
Orange, Gris très foncé, Blanc

```html
<!DOCTYPE html>
<html lang="fr">
<head>
<meta charset="utf-8">
<title>PrépaNova – Brochure</title>
<link href="https://fonts.googleapis.com/css2?family=Questrial&display=swap" rel="stylesheet">
<style>
  :root{
    --orange:#f07d1a;
    --dark:#3b3b3b;
    --white:#ffffff;
    --text-light:#e4e4e4;
    --text-dark:#555555;
    --ink:#2a2a2a;
  }
  *{margin:0;padding:0;box-sizing:border-box;}
  html,body{width:1200px;height:842px;overflow:hidden;background:var(--white);}
  body{font-family:"Questrial",sans-serif;font-size:11px;line-height:16px;}
  .spread{position:relative;width:1200px;height:842px;display:flex;}
  .page{position:relative;width:600px;height:842px;}
  .page--dark{background:var(--dark);color:var(--text-light);}
  .page--light{background:var(--white);color:var(--text-dark);}
  .tab{position:absolute;top:0;width:30px;height:14px;}
  .chevrons{position:absolute;bottom:26px;width:36px;height:22px;}
  .col{position:absolute;}
  .heading{color:var(--orange);font-size:12px;line-height:15px;margin-bottom:20px;}
  p{margin-bottom:20px;}
  .col--intro{left:106px;top:86px;width:190px;text-align:center;}
  .col--benefits{left:322px;top:86px;width:222px;}
  .benefits{list-style:none;margin-bottom:20px;}
  .benefits li{color:var(--white);margin-bottom:18px;}
  .col--sponsor{left:716px;top:54px;width:180px;text-align:right;}
  .col--sponsor .heading{margin-bottom:16px;}
  .questions{list-style:none;margin-bottom:6px;}
  .questions li{color:var(--ink);margin-bottom:12px;}
  .col--experts{left:910px;top:210px;width:196px;}
  .col--experts .heading{margin-bottom:8px;}
  .photo{position:absolute;}
  .photo--notebook{left:910px;top:50px;width:192px;height:156px;
    background:linear-gradient(135deg,#f2f2f0 0%,#d9dadd 55%,#9da3ab 100%);}
  .photo--student{left:700px;top:450px;width:186px;height:366px;
    background:linear-gradient(180deg,#e9e9e9 0%,#8a8a8a 35%,#5c5752 70%,#d7d2c8 100%);}
</style>
</head>
<body>
<div class="spread">
  <section class="page page--dark">
    <svg class="tab" style="left:276px" viewBox="0 0 30 14"><polygon points="0,0 30,0 15,14" fill="#ffffff"/></svg>

    <div class="col col--intro">
      <h2 class="heading">PrépaNova le partenaire de votre propre réussite</h2>
      <p>Pour vous accompagner dans votre préparation de concours, PrépaNova vous propose des cours particuliers de très haute qualité, dans les matières de mathématiques, de physique et de français. Les cours sont organisés par petit groupe et par groupe de niveau.</p>
      <p>Grâce à l'accompagnement de nos enseignants, vous allez acquérir les bases méthodologiques requises par les exigences des concours. Vous surmonterez plus facilement les difficultés d'apprentissage que vous pouvez rencontrer.</p>
      <p>L'un des points fort de notre encadrement, est d'apporter à chacun de vous, tout au long de l'année scolaire, l'accompagnement et le soutien moral qui vous est nécessaire afin que votre année de prépa se déroule dans la meilleure des façons et dans des conditions favorables, notamment à l'aide de nos conseils de travail et de programmes de révisions. Tout ceci vous permettra de mieux organiser les différentes périodes de votre année de sup ou de spé.</p>
    </div>

    <div class="col col--benefits">
      <h2 class="heading">L'efficacité des cours de soutien et de stages intensifs pour taupins</h2>
      <p>Grâce aux cours particuliers, vous, les étudiants des CPGE, vous pouvez acquérir des méthodes vous permettant d'atteindre vos objectifs.</p>
      <ul class="benefits">
        <li>+ Acquérir de bonnes méthodes de travail adaptées à chacune des matières principales.</li>
        <li>+ Conserver la motivation et la confiance tout au long de l'année scolaire.</li>
        <li>+ Effectuer des cours particuliers et des stages intensifs dans des locaux dotés d'outils aussi bien pédagogiques que technologiques.</li>
        <li>+ Préparer vos concours dans un établissement professionnel et structuré.</li>
      </ul>
      <p>Vous décidez vous-même du rythme. Il vous suffit de choisir un groupe ayant le même niveau que le vôtre pour profiter pleinement de vos séances d'apprentissage. Vous avez même la possibilité d'opter pour l'option « e-learning », qui permet de profiter des cours de soutien à distance depuis votre domicile, d'où un gain de temps notoire.</p>
    </div>

    <svg class="chevrons" style="left:540px" viewBox="0 0 36 22"><path d="M2 1l10 10-10 10M18 1l10 10-10 10" fill="none" stroke="#f07d1a" stroke-width="4"/></svg>
  </section>

  <section class="page page--light">
    <svg class="tab" style="left:266px" viewBox="0 0 30 14"><polygon points="0,0 30,0 15,14" fill="#3b3b3b"/></svg>
    <svg class="chevrons" style="left:528px" viewBox="0 0 36 22"><path d="M2 1l10 10-10 10M18 1l10 10-10 10" fill="none" stroke="#f07d1a" stroke-width="4"/></svg>
  </section>

  <div class="col col--sponsor">
    <h2 class="heading">Un encadrement basé sur une approche personnalisée.</h2>
    <p>Chez PrépaNova chacun de vous a un Sponsor, c'est un enseignant qui suit votre progrès tout au long de l'année scolaire. Il évalue vos progrès dans chacune des matières et vous propose les méthodes adéquates pour améliorer ou perfectionner votre niveau.</p>
    <ul class="questions">
      <li>• Quelles sont les chapitres que vous devez travailler pour combler vos lacunes ?</li>
      <li>• Combien de temps faut-il consacrer à chaque chapitre/matière ?</li>
      <li>• Quels objectifs faudrait-il viser ?</li>
    </ul>
    <p>Le sponsor est toujours joignable par mail ou par téléphone pour répondre à toutes vos questions...</p>
  </div>

  <div class="photo photo--notebook" role="img" aria-label="Photo d'un cahier de notes mathématiques avec un stylo"></div>

  <div class="col col--experts">
    <h2 class="heading">L'expertise d'enseignants et de très haute qualité</h2>
    <p>Les cours particuliers sont assurés par une équipe pédagogique exceptionnelle, les enseignants sont des professeurs de classes préparatoires publics ou privés, cette équipe est complétée par des enseignants issus des meilleurs écoles françaises (POLYTEKNA, Normale Arcadia, Centrale Lumière, les MINES de Valmont et les ARCHES. L'ensemble de notre personnel connaît parfaitement le monde des CPGE et des concours. Il dispose d'outils spécifiques et de toutes les ressources pédagogiques adéquates pour proposer un enseignement de haute qualité.</p>
  </div>

  <div class="photo photo--student" role="img" aria-label="Photo d'une étudiante lisant une pile de livres"></div>
</div>
</body>
</html>
```